A Bold and Enticing Book Cover is needed for my new book Bright Harbor!

I need a Book Cover Design for my paperback book that will be published next Spring... The book is called:

Bright Harbor
A Pocket Map for Turning Points and Endings

I want the design to be bold and eye-catching, and not too soft or touchy feely! I'd like the fonts to be funky, and clear. I feel that the design should capture the idea of moving forwards and growth. I am a Solution Focused Hypnotherapist, and our model of therapy is direct, but also supports change in a step by step solution focused way!

I'm uploading an idea, but am so open to suggestions.

I really like the design of the BRIGHT HARBOR lettering I have used...

Looking forward to seeing your suggestions!

Thanks,

Renka :)

Target Market(s)

Readers and Browsers who are grieving or going through change...

Industry/Entity Type

Hypnotherapy

Font styles to use
Sans Serif
Other font styles liked:
• star avenue?

Requirements
Must have
• Be Bold, and Eyecatching... Maybe reference to the Brain, as I'm a hypnotherapist.
Nice to have
• Bright Colour... My website is bold, look at that www.themarlowenstudio.example but please don't just copy images off the website... I want it to have a 'feel' of the website, but not be a replica!
Should not have
• I'm not into fluffy or pastel images...

```html
<!DOCTYPE html>
<html lang="en">
<head>
<meta charset="utf-8">
<title>Bright Harbor — Book Cover</title>
<link href="https://fonts.googleapis.com/css2?family=Jost:wght@300;700;800&display=swap" rel="stylesheet">
<style>
  :root {
    --teal-deep: #175a61;
    --teal-mid: #2a8589;
    --teal-light: #3a9c9f;
    --ink: #ffffff;
  }
  * { margin: 0; padding: 0; box-sizing: border-box; }
  html, body {
    width: 800px;
    height: 1200px;
    overflow: hidden;
    background: var(--teal-deep);
  }
  .cover {
    position: relative;
    width: 800px;
    height: 1200px;
    background: radial-gradient(ellipse 80% 62% at 50% 45%, var(--teal-light) 0%, var(--teal-mid) 48%, var(--teal-deep) 100%);
    color: var(--ink);
    font-family: 'Jost', sans-serif;
    text-align: center;
    overflow: hidden;
  }
  .title { font-weight: normal; }
  .title-main {
    position: absolute;
    top: 90px;
    left: 0;
    width: 100%;
    font-weight: 800;
    font-size: 162px;
    line-height: 1;
    letter-spacing: 0.01em;
  }
  .title-sub {
    position: absolute;
    top: 256px;
    left: 0;
    width: 100%;
    font-weight: 300;
    font-size: 160px;
    line-height: 1;
    letter-spacing: 0.05em;
  }
  .subtitle {
    position: absolute;
    top: 480px;
    left: 0;
    width: 100%;
    font-weight: 700;
    font-size: 29px;
    line-height: 1.2;
  }
  .artwork {
    position: absolute;
    top: 540px;
    left: 0;
    width: 800px;
    height: 500px;
  }
  .author {
    position: absolute;
    top: 1052px;
    left: 0;
    width: 100%;
    font-weight: 700;
    font-size: 84px;
    line-height: 1;
    letter-spacing: 0.02em;
  }
</style>
</head>
<body>
  <main class="cover">
    <h1 class="title">
      <span class="title-main">BRIGHT</span>
      <span class="title-sub">HARBOR</span>
    </h1>
    <p class="subtitle">A Pocket Map for Turning Points and Endings</p>

    <svg class="artwork" viewBox="0 0 800 500" role="img" aria-label="Illustration of a teal human brain with a glowing white dove taking flight from it">
      <defs>
        <radialGradient id="brainTone">
          <stop offset="0%" stop-color="#5ab3b4" stop-opacity="0.85"/>
          <stop offset="60%" stop-color="#4aa3a5" stop-opacity="0.5"/>
          <stop offset="100%" stop-color="#3a9c9f" stop-opacity="0"/>
        </radialGradient>
        <radialGradient id="doveGlow">
          <stop offset="0%" stop-color="#ffffff" stop-opacity="1"/>
          <stop offset="30%" stop-color="#ffffff" stop-opacity="0.75"/>
          <stop offset="65%" stop-color="#e8f6f6" stop-opacity="0.25"/>
          <stop offset="100%" stop-color="#ffffff" stop-opacity="0"/>
        </radialGradient>
      </defs>
      <ellipse class="brain-area" cx="330" cy="270" rx="210" ry="170" fill="url(#brainTone)"/>
      <ellipse class="dove-area" cx="500" cy="250" rx="190" ry="230" fill="url(#doveGlow)"/>
    </svg>

    <p class="author">RENKA HALDEN</p>
  </main>
</body>
</html>
```